Creating a visual for the various stage of our Packets by Locations: *Memphis Region *Clinics in TRV School District*Nashville Region *Knoxville Region. The attached file contains two tabs the layout of the packet scheme that currently in place and a second tab with the definition of the various cells that is needed as a legend on each report. The goal is to get the report tab an easily "eye" visual for the CEO of the company to follow. Create a Reporting Dashboard Template that we can input number into easily to update. The color scheme should reflect our website www.brightsprout.example
Target Market(s)
Pediatric company that performs BrightSprout Exams and Optometry exams in school districts
Industry/Entity Type
Healthcare
Requirements
Must have
- Printable dash page. You can use this file and add a dash page that flows from the report page as an option in excel
Nice to have
- maybe 3D modern feel with the color scheme of the company website

```html
<!DOCTYPE html>
<html lang="en">
<head>
<meta charset="utf-8">
<title>BrightSprout – Packet Reporting Dashboard &amp; Definitions</title>
<link href="https://fonts.googleapis.com/css2?family=Roboto+Condensed:wght@400;700&family=Montserrat:wght@800&display=swap" rel="stylesheet">
<style>
:root{
  --page:#ececec;
  --blue:#0b5cab;
  --blue-deep:#094e93;
  --blue-line:#4f8fd3;
  --ink:#1c1c1c;
  --navy:#1f2f5a;
  --panel-grey:#d9d9d9;
  --row-grey:#f1f1f1;
  --c-blue:#1a73d9;
  --c-red:#d0202e;
  --c-yellow:#f2b705;
  --c-green:#0e9a7a;
  --c-teal:#36c3c9;
  --body:"Roboto Condensed",Arial,sans-serif;
}
*{box-sizing:border-box;margin:0;padding:0}
html,body{width:907px;height:1200px;overflow:hidden}
body{background:var(--page);font-family:var(--body);color:var(--ink);position:relative}

/* ---------- shared ---------- */
.brand{display:flex;align-items:center;justify-content:center;gap:8px;color:#fff;font-family:var(--body);font-weight:400}
.brand-dot{border-radius:50%;background:#fff;display:block}
.caption{position:absolute;top:1138px;font-family:"Montserrat",sans-serif;font-weight:800;font-size:30px;color:var(--navy);letter-spacing:.5px;text-align:center}

/* ---------- report sheet ---------- */
.report{position:absolute;left:96px;top:28px;width:380px;height:1092px;background:#fff;box-shadow:0 2px 6px rgba(0,0,0,.25);overflow:hidden}
.report-header{position:absolute;left:0;top:0;width:380px;height:68px;background:var(--blue);border-top:3px solid var(--blue-line)}
.report-header .brand{height:62px;font-size:32px}
.report-header .brand-dot{width:22px;height:22px}
.report-header::after{content:"";position:absolute;left:0;right:0;bottom:3px;height:1px;background:#fff}
.report-notch{position:absolute;left:0;top:66px}

.region-frame{position:absolute;left:9px;top:106px;width:362px;height:448px;border:1.5px solid var(--ink)}
.region-title{position:absolute;left:0;right:0;top:-7px;text-align:center}
.region-title span{background:#fff;padding:0 3px;font-size:10px;font-weight:700}

.step-tag{position:absolute;left:14px;height:11px;background:var(--blue);color:#fff;font-size:5px;font-weight:700;line-height:11px;padding:0 10px 0 17px;border-radius:0 6px 6px 0}
.step-tag i{position:absolute;left:-1px;top:-1px;width:13px;height:13px;border-radius:50%;background:var(--blue);border:1.5px solid #fff;box-shadow:0 0 0 1px var(--blue);font-style:normal;text-align:center;line-height:10px;font-size:5px}

.sheet-table{position:absolute;left:18px;width:343px;border:1px solid var(--blue);font-size:6.5px}
.sheet-table .head{display:grid;background:var(--blue);color:#fff;font-size:4.6px;height:16px;align-items:center;text-align:center;line-height:1.1}
.sheet-table .head div{border-right:1px solid #fff;height:100%;display:flex;align-items:center;justify-content:center}
.sheet-table .head div:last-child{border-right:none}
.sheet-table .vals{display:grid;height:19px;align-items:center;text-align:center;font-weight:700}
.sheet-table .vals.alt{background:var(--row-grey);height:26px;border-top:1px solid #ddd}
.sheet-table .vals .note{font-size:4.6px;font-weight:400;line-height:1.1}
.cols-8{grid-template-columns:repeat(8,1fr)}
.cols-4{grid-template-columns:84fr 86fr 86fr 87fr}
.cols-3{grid-template-columns:106fr 123fr 113fr}
.cols-1{grid-template-columns:1fr}

/* ---------- memphis block ---------- */
.memphis-band{position:absolute;left:0;top:560px}
.memphis-tab{position:absolute;left:4px;top:602px;height:14px;width:138px;background:#fff;color:var(--blue);font-size:9.5px;font-weight:700;line-height:14px;padding-left:6px;clip-path:polygon(0 0,100% 0,92% 100%,0 100%)}
.rail{position:absolute;left:9px;width:1px;background:#fff}
.m-head{position:absolute;left:86px;top:632px;width:284px;display:grid;grid-template-columns:repeat(8,1fr);gap:2px}
.m-head div{background:#fff;color:var(--blue);font-size:3.8px;text-align:center;height:13px;display:flex;align-items:center;justify-content:center;line-height:1.05}
.m-grid{position:absolute;left:86px;width:284px;display:grid;grid-template-columns:repeat(8,1fr);color:#fff;font-size:5px;text-align:center;align-items:center}
.m-grid .note{font-size:4.3px;font-weight:700;line-height:1.1}
.m-stripe{position:absolute;left:10px;width:370px;background:var(--blue-deep)}
.m-label{position:absolute;left:26px;color:#fff;font-size:5px;font-weight:700;line-height:1.15}
.step-dot{position:absolute;left:5px;width:9px;height:9px;border-radius:50%;background:var(--blue);border:1px solid #fff;color:#fff;font-size:4.5px;text-align:center;line-height:7px}
.sy-pill{display:inline-block;background:#fff;color:var(--blue);font-size:3.6px;border-radius:3px;padding:0 3px;line-height:6px}

/* ---------- combined block ---------- */
.combined-title{position:absolute;left:0;top:902px;width:372px;height:17px;background:var(--blue);color:#fff;font-size:9.5px;line-height:17px;padding-left:10px;clip-path:polygon(0 0,100% 0,97% 100%,0 100%)}
.c-row{position:absolute;left:10px;width:370px;height:34px}
.c-row.alt{background:#f6f6f6}
.c-row .c-label{position:absolute;left:16px;top:50%;transform:translateY(-50%);font-size:5px;font-weight:700;line-height:1.2}
.c-row .c-val{position:absolute;left:164px;top:50%;transform:translateY(-50%);font-size:5px;color:var(--blue)}
.c-row .step-dot{left:-5px;top:50%;transform:translateY(-50%)}
.rail.dark{background:var(--blue)}
.report-foot{position:absolute;left:0;bottom:0;width:380px;height:8px;background:var(--blue);border-top:1px solid #fff;box-shadow:0 -1px 0 var(--blue)}

/* ---------- definitions sheet ---------- */
.legend{position:absolute;left:614px;top:30px;width:191px;height:1092px;background:var(--panel-grey);box-shadow:0 2px 6px rgba(0,0,0,.25);overflow:hidden}
.legend-header{position:absolute;left:0;top:0;width:191px;height:38px;background:var(--blue);border-top:3px solid var(--blue-line)}
.legend-header .brand{height:30px;font-size:16px;gap:5px}
.legend-header .brand-dot{width:11px;height:11px}
.legend-header::after{content:"";position:absolute;left:0;right:0;bottom:2px;height:1px;background:#fff}
.legend-shapes{position:absolute;left:0;top:0}
.legend-title{position:absolute;left:0;right:0;top:57px;text-align:center;color:var(--blue);font-size:6px;font-weight:700}
.legend-intro{position:absolute;left:6px;right:6px;top:105px;text-align:center;font-size:4.8px;font-weight:700;line-height:1.3;color:#333}
.def-text{position:absolute;left:78px;width:74px;font-size:3.1px;line-height:1.25;color:#444}
.forecast-text{position:absolute;left:57px;width:76px;top:601px;text-align:center;font-size:3.6px;font-weight:700;color:var(--blue);line-height:1.25}
.branch-text{position:absolute;width:30px;top:683px;text-align:center;font-size:2.9px;line-height:1.3;color:var(--blue)}
.chain-text{position:absolute;color:#fff;font-size:3.8px;font-weight:700;text-align:center;line-height:1.3}
</style>
</head>
<body>

<!-- ================= REPORT SHEET ================= -->
<section class="report" aria-label="Packet report">
  <header class="report-header">
    <div class="brand"><span class="brand-dot"></span>BrightSprout</div>
  </header>
  <svg class="report-notch" width="380" height="30" viewBox="0 0 380 30"><polygon points="158,0 222,0 190,28" fill="var(--blue)"/></svg>

  <div class="region-frame"><div class="region-title"><span>NASHVILLE &amp; KNOXVILLE</span></div></div>

  <!-- step 1 -->
  <div class="step-tag" style="top:121px"><i>1</i>AX SYSTEM VS. PACKET TRACKING SYSTEM</div>
  <div class="sheet-table" style="top:142px">
    <div class="head cols-8"><div>CALL CENTER<br>PACKETS</div><div>COMPLETE<br>PACKETS</div><div>DUPLICATES<br>PACKETS</div><div>INCOMPLETE<br>PACKETS</div><div>NO SIGNATURE<br>PACKETS</div><div>DECLINE<br>PACKETS</div><div>BLANKS<br>PACKETS</div><div>(OVER)/UNDER<br>ESTIMATED</div></div>
    <div class="vals cols-8"><div>49</div><div>22,454</div><div>468</div><div>919</div><div>-</div><div>1034</div><div>489</div><div>-</div></div>
    <div class="vals alt cols-8"><div></div><div></div><div class="note">TOTAL<br>PACKETS</div><div>25,364</div><div class="note">PACKETS TRACKING<br>SYSTEM</div><div>23,349</div><div>489</div><div>2,015</div></div>
  </div>

  <!-- step 2 -->
  <div class="step-tag" style="top:223px"><i>2</i>INSURED PACKETS</div>
  <div class="sheet-table" style="top:245px">
    <div class="head cols-4"><div>CALL CENTER PACKETS</div><div>COMPLETE PACKETS</div><div>DUPLICATES PACKETS</div><div>UNINSURED PACKETS</div></div>
    <div class="vals cols-4"><div>49</div><div>22,405</div><div></div><div>5944</div></div>
    <div class="vals alt cols-4"><div></div><div class="note">INSURED PACKETS</div><div>16,510</div><div></div></div>
  </div>

  <!-- step 3 -->
  <div class="step-tag" style="top:325px"><i>3</i>INSURED COMPLETED EXAMS OUT OF COMPLETED PACKETS</div>
  <div class="sheet-table" style="top:346px">
    <div class="head cols-1"><div>DUPLICATES PACKETS</div></div>
    <div class="vals cols-1"><div>3718</div></div>
  </div>

  <!-- step 4 -->
  <div class="step-tag" style="top:405px"><i>4</i>LEFT BEHIND/TO COMPLETE</div>
  <div class="sheet-table" style="top:426px">
    <div class="head cols-1"><div>DUPLICATES PACKETS</div></div>
    <div class="vals cols-1"><div>12,792</div></div>
  </div>

  <!-- step 5 -->
  <div class="step-tag" style="top:483px"><i>5</i>COMPARISON OF INSURED PACKETS 2017-18 VS. 2018-19</div>
  <div class="sheet-table" style="top:504px">
    <div class="head cols-3"><div>2017 - 2018</div><div>2018 - 2019</div><div>UNINSURED PACKETS</div></div>
    <div class="vals cols-3"><div>22,354</div><div>16,510</div><div>5,844</div></div>
  </div>

  <!-- ---------- Memphis ---------- -->
  <svg class="memphis-band" width="380" height="340" viewBox="0 0 380 340">
    <polygon points="0,0 190,34 380,0 380,296 190,328 0,296" fill="var(--blue)"/>
    <polyline points="182,12 190,17 198,12" fill="none" stroke="#fff" stroke-width="1"/>
    <polyline points="182,310 190,315 198,310" fill="none" stroke="#fff" stroke-width="1"/>
  </svg>
  <div class="memphis-tab">MEMPHIS MOBILE / CLINICS</div>
  <div class="rail" style="top:618px;height:235px"></div>

  <div class="m-stripe" style="top:701px;height:45px"></div>
  <div class="m-stripe" style="top:788px;height:32px"></div>

  <div class="m-head"><div>CALL CENTER<br>PACKETS</div><div>COMPLETE<br>PACKETS</div><div>DUPLICATES<br>PACKETS</div><div>INCOMPLETE<br>PACKETS</div><div>NO SIGNATURE<br>PACKETS</div><div>DECLINE<br>PACKETS</div><div>BLANKS<br>PACKETS</div><div>(OVER)/UNDER<br>ESTIMATED</div></div>

  <span class="step-dot" style="top:673px">1</span>
  <div class="m-label" style="top:662px">AX SYSTEM VS.<br>PACKET TRACKING<br>SYSTEM</div>
  <div class="m-grid" style="top:653px"><div>13984</div><div>15843</div><div>2776</div><div>1646</div><div></div><div>2776</div><div>384</div><div></div></div>
  <div class="m-grid" style="top:669px"><div></div><div></div><div class="note">TOTAL PACKETS</div><div>29,827</div><div class="note">TOTAL PACKETS<br>TRACKING SYSTEM</div><div>37409</div><div></div><div>7582</div></div>

  <span class="step-dot" style="top:709px">2</span>
  <div class="m-label" style="top:711px">INSURED PACKETS</div>
  <div class="m-grid" style="top:709px"><div>13984</div><div>15843</div><div></div><div>1646</div><div></div><div></div><div></div><div>7361</div></div>
  <div class="m-grid" style="top:725px"><div></div><div class="note">INSURED<br>PACKETS</div><div>22,466</div></div>

  <span class="step-dot" style="top:767px">3</span>
  <div class="m-label" style="top:759px">INSURED COMPLETED<br>EXAMS OUT OF<br>COMPLETED PACKETS</div>
  <div class="m-grid" style="top:768px"><div></div><div></div><div>6107</div></div>

  <span class="step-dot" style="top:800px">4</span>
  <div class="m-label" style="top:799px">LEFT BEHIND /<br>TO COMPLETE</div>
  <div class="m-grid" style="top:801px"><div></div><div></div><div>16359</div></div>

  <span class="step-dot" style="top:834px">5</span>
  <div class="m-label" style="top:832px">COMPARISON OF<br>INSURED PACKETS</div>
  <div class="m-grid" style="top:834px"><div>30538</div><div>22466</div><div>8072</div></div>
  <div class="m-grid" style="top:847px"><div><span class="sy-pill">SY 2017-18</span></div><div><span class="sy-pill">SY 2018-19</span></div></div>

  <!-- ---------- combined ---------- -->
  <div class="combined-title">COMBINED NEED ANALYSIS MEMPHIS MOBILE/CLINICS, NASHVILLE, KNOXVILLE</div>
  <div class="rail dark" style="top:919px;height:160px"></div>
  <div class="c-row" style="top:920px"><span class="step-dot">6</span><div class="c-label">TOTAL GROSS PACKETS<br>RECEIVED STATEWIDE</div><div class="c-val">55,191</div></div>
  <div class="c-row alt" style="top:958px"><span class="step-dot">7</span><div class="c-label">TOTAL INSURED PACKETS<br>RECEIVED STATEWIDE</div><div class="c-val">38,976</div></div>
  <div class="c-row" style="top:996px"><span class="step-dot">8</span><div class="c-label">STATEWIDE EPSDT NEEDS<br>FOR INSURED PACKETS</div><div class="c-val">13,916</div></div>
  <div class="c-row alt" style="top:1036px"><span class="step-dot">9</span><div class="c-label">GROSS PACKET NEEDS TO<br>CONVERT INTO INSURED<br>PACKETS @ 29% OF STEP 6</div><div class="c-val">17,952</div></div>
  <div class="report-foot"></div>
</section>

<!-- ================= DEFINITIONS SHEET ================= -->
<section class="legend" aria-label="Definitions of stages for a packet">
  <header class="legend-header">
    <div class="brand"><span class="brand-dot"></span>BrightSprout</div>
  </header>

  <svg class="legend-shapes" width="191" height="1092" viewBox="0 0 191 1092" font-family="Roboto Condensed, Arial, sans-serif">
    <!-- stage 1 badge -->
    <circle cx="95" cy="90" r="11" fill="#fff" stroke="var(--c-yellow)" stroke-width="2"/>
    <text x="95" y="94" text-anchor="middle" font-size="11" font-weight="700" fill="var(--navy)">1</text>

    <!-- definition rows -->
    <g id="def-rows" font-size="11" font-weight="700" text-anchor="middle">
      <g transform="translate(0,142)"><rect x="66" y="-12" width="90" height="24" rx="12" fill="#fff"/><line x1="8" y1="0" x2="50" y2="0" stroke="var(--c-blue)" stroke-width="2.5"/><circle cx="40" cy="0" r="2.5" fill="#fff" stroke="var(--c-blue)"/><circle cx="60" cy="0" r="11" fill="#fff" stroke="var(--c-blue)" stroke-width="3"/><text x="60" y="4" fill="var(--navy)">A</text></g>
      <g transform="translate(0,177)"><rect x="66" y="-12" width="90" height="24" rx="12" fill="#fff"/><line x1="8" y1="0" x2="50" y2="0" stroke="var(--c-red)" stroke-width="2.5"/><circle cx="40" cy="0" r="2.5" fill="#fff" stroke="var(--c-red)"/><circle cx="60" cy="0" r="11" fill="#fff" stroke="var(--c-red)" stroke-width="3"/><text x="60" y="4" fill="var(--navy)">B</text></g>
      <g transform="translate(0,212)"><rect x="66" y="-12" width="90" height="24" rx="12" fill="#fff"/><line x1="8" y1="0" x2="50" y2="0" stroke="var(--c-yellow)" stroke-width="2.5"/><circle cx="40" cy="0" r="2.5" fill="#fff" stroke="var(--c-yellow)"/><circle cx="60" cy="0" r="11" fill="#fff" stroke="var(--c-yellow)" stroke-width="3"/><text x="60" y="4" fill="var(--navy)">C</text></g>
      <g transform="translate(0,247)"><rect x="66" y="-12" width="90" height="24" rx="12" fill="#fff"/><line x1="8" y1="0" x2="50" y2="0" stroke="var(--c-green)" stroke-width="2.5"/><circle cx="40" cy="0" r="2.5" fill="#fff" stroke="var(--c-green)"/><circle cx="60" cy="0" r="11" fill="#fff" stroke="var(--c-green)" stroke-width="3"/><text x="60" y="4" fill="var(--navy)">D</text></g>
      <g transform="translate(0,282)"><rect x="66" y="-12" width="90" height="24" rx="12" fill="#fff"/><line x1="8" y1="0" x2="50" y2="0" stroke="var(--c-blue)" stroke-width="2.5"/><circle cx="40" cy="0" r="2.5" fill="#fff" stroke="var(--c-blue)"/><circle cx="60" cy="0" r="11" fill="#fff" stroke="var(--c-blue)" stroke-width="3"/><text x="60" y="4" fill="var(--navy)">E</text></g>
      <g transform="translate(0,317)"><rect x="66" y="-12" width="90" height="24" rx="12" fill="#fff"/><line x1="8" y1="0" x2="50" y2="0" stroke="var(--c-red)" stroke-width="2.5"/><circle cx="40" cy="0" r="2.5" fill="#fff" stroke="var(--c-red)"/><circle cx="60" cy="0" r="11" fill="#fff" stroke="var(--c-red)" stroke-width="3"/><text x="60" y="4" fill="var(--navy)">F</text></g>
      <g transform="translate(0,352)"><rect x="66" y="-12" width="90" height="24" rx="12" fill="#fff"/><line x1="8" y1="0" x2="50" y2="0" stroke="var(--c-yellow)" stroke-width="2.5"/><circle cx="40" cy="0" r="2.5" fill="#fff" stroke="var(--c-yellow)"/><circle cx="60" cy="0" r="11" fill="#fff" stroke="var(--c-yellow)" stroke-width="3"/><text x="60" y="4" fill="var(--navy)">G</text></g>
      <g transform="translate(0,387)"><rect x="66" y="-12" width="90" height="24" rx="12" fill="#fff"/><line x1="8" y1="0" x2="50" y2="0" stroke="var(--c-green)" stroke-width="2.5"/><circle cx="40" cy="0" r="2.5" fill="#fff" stroke="var(--c-green)"/><circle cx="60" cy="0" r="11" fill="#fff" stroke="var(--c-green)" stroke-width="3"/><text x="60" y="4" fill="var(--navy)">H</text></g>
      <g transform="translate(0,422)"><rect x="66" y="-12" width="90" height="24" rx="12" fill="#fff"/><line x1="8" y1="0" x2="50" y2="0" stroke="var(--c-blue)" stroke-width="2.5"/><circle cx="40" cy="0" r="2.5" fill="#fff" stroke="var(--c-blue)"/><circle cx="60" cy="0" r="11" fill="#fff" stroke="var(--c-blue)" stroke-width="3"/><text x="60" y="4" fill="var(--navy)">I</text></g>
      <g transform="translate(0,457)"><rect x="66" y="-12" width="90" height="24" rx="12" fill="#fff"/><line x1="8" y1="0" x2="50" y2="0" stroke="var(--c-red)" stroke-width="2.5"/><circle cx="40" cy="0" r="2.5" fill="#fff" stroke="var(--c-red)"/><circle cx="60" cy="0" r="11" fill="#fff" stroke="var(--c-red)" stroke-width="3"/><text x="60" y="4" fill="var(--navy)">J</text></g>
      <g transform="translate(0,492)"><rect x="66" y="-12" width="90" height="24" rx="12" fill="#fff"/><line x1="8" y1="0" x2="50" y2="0" stroke="var(--c-yellow)" stroke-width="2.5"/><circle cx="40" cy="0" r="2.5" fill="#fff" stroke="var(--c-yellow)"/><circle cx="60" cy="0" r="11" fill="#fff" stroke="var(--c-yellow)" stroke-width="3"/><text x="60" y="4" fill="var(--navy)">H</text></g>
    </g>

    <!-- stage 2 forecast -->
    <circle cx="95" cy="578" r="52" fill="#fff"/>
    <circle cx="95" cy="578" r="46" fill="none" stroke="var(--c-green)" stroke-width="6" stroke-dasharray="36 253" stroke-dashoffset="0"/>
    <circle cx="95" cy="578" r="46" fill="none" stroke="var(--c-yellow)" stroke-width="6" stroke-dasharray="36 253" stroke-dashoffset="-36"/>
    <circle cx="95" cy="578" r="46" fill="none" stroke="var(--c-red)" stroke-width="6" stroke-dasharray="36 253" stroke-dashoffset="-72"/>
    <circle cx="95" cy="578" r="46" fill="none" stroke="var(--c-blue)" stroke-width="6" stroke-dasharray="36.5 253" stroke-dashoffset="-108"/>
    <text x="95" y="598" text-anchor="middle" font-size="20" font-weight="700" fill="var(--blue)" transform="translate(0,-30)">2</text>

    <g fill="none" stroke="#777" stroke-width="0.8">
      <polyline points="26,650 26,603 44,603"/>
      <polyline points="166,650 166,603 146,603"/>
      <line x1="72" y1="628" x2="72" y2="650"/>
      <line x1="119" y1="628" x2="119" y2="650"/>
    </g>
    <g font-size="8" font-weight="700" text-anchor="middle" fill="var(--navy)">
      <rect x="9" y="652" width="34" height="92" rx="17" fill="#fff" stroke="var(--c-blue)" stroke-width="2"/><circle cx="26" cy="669" r="9" fill="#fff" stroke="var(--c-blue)" stroke-width="2"/><text x="26" y="672">A</text>
      <rect x="55" y="652" width="34" height="92" rx="17" fill="#fff" stroke="var(--c-red)" stroke-width="2"/><circle cx="72" cy="669" r="9" fill="#fff" stroke="var(--c-red)" stroke-width="2"/><text x="72" y="672">B</text>
      <rect x="102" y="652" width="34" height="92" rx="17" fill="#fff" stroke="var(--c-yellow)" stroke-width="2"/><circle cx="119" cy="669" r="9" fill="#fff" stroke="var(--c-yellow)" stroke-width="2"/><text x="119" y="672">C</text>
      <rect x="149" y="652" width="34" height="92" rx="17" fill="#fff" stroke="var(--c-green)" stroke-width="2"/><circle cx="166" cy="669" r="9" fill="#fff" stroke="var(--c-green)" stroke-width="2"/><text x="166" y="672">D</text>
    </g>

    <!-- stages 3–9 chain -->
    <g>
      <rect x="66" y="772" width="113" height="27" rx="13.5" fill="var(--c-blue)"/>
      <rect x="6" y="818" width="112" height="27" rx="13.5" fill="var(--c-red)"/>
      <rect x="66" y="861" width="118" height="28" rx="14" fill="var(--c-yellow)"/>
      <rect x="6" y="902" width="112" height="27" rx="13.5" fill="var(--c-green)"/>
      <rect x="66" y="945" width="113" height="27" rx="13.5" fill="var(--c-teal)"/>
      <rect x="6" y="991" width="112" height="27" rx="13.5" fill="var(--c-blue)"/>
      <rect x="50" y="1030" width="130" height="32" rx="16" fill="var(--c-yellow)"/>
    </g>
    <g font-size="17" font-weight="700" text-anchor="middle">
      <circle cx="56" cy="786" r="23" fill="#fff" stroke="var(--c-blue)" stroke-width="6"/><text x="56" y="792" fill="var(--c-blue)">3</text>
      <circle cx="134" cy="831" r="23" fill="#fff" stroke="var(--c-red)" stroke-width="6"/><text x="134" y="837" fill="var(--c-red)">4</text>
      <circle cx="56" cy="875" r="23" fill="#fff" stroke="var(--c-yellow)" stroke-width="6"/><text x="56" y="881" fill="var(--c-yellow)">5</text>
      <circle cx="134" cy="915" r="23" fill="#fff" stroke="var(--c-green)" stroke-width="6"/><text x="134" y="921" fill="var(--c-green)">6</text>
      <circle cx="56" cy="959" r="23" fill="#fff" stroke="var(--c-teal)" stroke-width="6"/><text x="56" y="965" fill="var(--c-teal)">7</text>
      <circle cx="134" cy="1004" r="23" fill="#fff" stroke="var(--c-blue)" stroke-width="6"/><text x="134" y="1010" fill="var(--c-blue)">8</text>
      <circle cx="36" cy="1046" r="28" fill="#fff" stroke="var(--c-yellow)" stroke-width="6"/><text x="36" y="1052" fill="var(--c-yellow)">9</text>
    </g>
  </svg>

  <div class="legend-title">DEFINTIONS OF STAGES <span style="font-weight:400">FOR A PACKET</span></div>
  <p class="legend-intro">This represents the comparisons of Completed Packets in AX vs Packet Tracking Gross Packets Received by Outreach</p>

  <p class="def-text" style="top:137px">Cell C4: call center packets completed count</p>
  <p class="def-text" style="top:172px">Cell D4: complete packets through the HIC cycle</p>
  <p class="def-text" style="top:207px">Cell E4: duplicate packets scanned more than once</p>
  <p class="def-text" style="top:242px">Cell F4: incomplete packets missing required child history</p>
  <p class="def-text" style="top:277px">Cell D4: complete packets ready for EPSDT screening</p>
  <p class="def-text" style="top:312px">Cell H4: guardian declined service on packet</p>
  <p class="def-text" style="top:347px">Cell I4: blank packets not scanned into AX</p>
  <p class="def-text" style="top:382px">Cell F5: total packets minus call center packets</p>
  <p class="def-text" style="top:417px">Cell D5: total packets plus complete packets</p>
  <p class="def-text" style="top:452px">Cell H5: packets received in the tracking system</p>
  <p class="def-text" style="top:487px">Cell J5: difference between AX and tracking system</p>

  <p class="forecast-text" style="top:570px">Insured Packets step gives an forecast of how many insured EPSDT screening from the call center and completed packets minus the uninsured packets received</p>

  <p class="branch-text" style="left:11px">Insured packets forecast from call center and completed packets</p>
  <p class="branch-text" style="left:57px">Call center plus complete packets minus uninsured Memphis</p>
  <p class="branch-text" style="left:104px">Memphis total including incomplete and unsigned packets</p>
  <p class="branch-text" style="left:151px">Call center plus complete packets minus uninsured Nashville</p>

  <p class="chain-text" style="left:82px;top:778px;width:94px">Number of Completed exams for current School Year from billing report</p>
  <p class="chain-text" style="left:12px;top:822px;width:96px">Left Behind/to Complete represents the number of available EPSDT screening to perform or unable to reach</p>
  <p class="chain-text" style="left:82px;top:868px;width:98px">Comparison of Insured Packets 2017-18 vs. 2018-19</p>
  <p class="chain-text" style="left:12px;top:908px;width:96px">Total gross packets received statewide = MEM + NASH</p>
  <p class="chain-text" style="left:82px;top:951px;width:94px">Total insured packets received statewide = MEM + NASH</p>
  <p class="chain-text" style="left:12px;top:997px;width:96px">Statewide EPSDT Needs for Insured Packets = E16 + E32</p>
  <p class="chain-text" style="left:72px;top:1038px;width:104px">Gross Packet Needs to convert into Insured Packets at 29% of Step 6</p>
</section>

<div class="caption" style="left:186px;width:200px">REPORT</div>
<div class="caption" style="left:600px;width:220px">DEFINATION</div>

</body>
</html>
```